Dorvo Letterhead

Hi I really like the attached pictures for our business cards could you please look at designing something similar for our letterheads and stationary.

The details on our letterhead will be

Dorvo Pty Ltd
ABN 418 276 530
PO Box 7214
Kellan Ridge NSW 2871
0472 318 605
office"dorvo.com.au

```html
<!DOCTYPE html>
<html lang="en">
<head>
<meta charset="utf-8">
<title>Dorvo Letterhead</title>
<link rel="stylesheet" href="https://fonts.googleapis.com/css2?family=Roboto:wght@400;500;700&family=Tinos&display=swap">
<style>
  :root {
    --backdrop: #707070;
    --paper: #efefef;
    --ink: #333333;
    --ink-dark: #111111;
    --brand-blue: #3f78c0;
    --rule: #bdbdbd;
    --flap-top: #3a6fc0;
    --flap-bottom: #1a1a1a;
    --watermark: rgba(190, 198, 212, 0.35);
  }
  * { box-sizing: border-box; margin: 0; padding: 0; }
  html, body { width: 1200px; height: 947px; overflow: hidden; }
  body { background: var(--backdrop); position: relative; font-family: "Roboto", sans-serif; }

  .sheet { position: absolute; background: var(--paper); overflow: hidden; }

  .letterhead {
    left: 72px; top: 82px; width: 553px; height: 782px;
    box-shadow: 0 2px 10px rgba(0,0,0,0.35);
  }
  .watermark-area {
    position: absolute; z-index: 0;
    background: linear-gradient(135deg, transparent 0%, var(--watermark) 40%, rgba(215,220,230,0.25) 70%, transparent 100%);
  }
  .letterhead .watermark-area { left: 0; top: 370px; width: 500px; height: 390px; }

  .brand-name {
    position: absolute; z-index: 1; font-family: "Roboto", sans-serif; font-weight: 700;
    color: var(--ink-dark); letter-spacing: 1px;
  }
  .letterhead .brand-name { left: 62px; top: 78px; font-size: 36px; }
  .contact-block {
    position: absolute; z-index: 1; left: 400px; top: 55px; padding-left: 10px;
    border-left: 1px solid var(--rule);
    font-size: 7.6px; line-height: 9.6px; color: var(--ink); font-style: normal;
  }
  .company { color: var(--brand-blue); font-weight: 500; }

  .letter-body {
    position: absolute; z-index: 1; left: 61px; top: 195px; width: 431px;
    font-family: "Tinos", serif; color: var(--ink); font-size: 8.3px; line-height: 12px;
  }
  .letter-date { font-size: 9.6px; margin-bottom: 25px; }
  .recipient { font-size: 9.6px; line-height: 12px; margin-bottom: 22px; }
  .letter-body p.para { text-align: justify; margin-bottom: 12px; }
  .signature {
    position: absolute; z-index: 1; left: 62px; top: 540px; width: 110px; height: 40px;
    background: linear-gradient(90deg, rgba(120,120,120,0.18), rgba(120,120,120,0.05));
  }

  .footer-band { position: absolute; z-index: 1; left: 0; right: 0; bottom: 0; height: 24px; }
  .footer-band svg { position: absolute; left: 0; top: 0; width: 100%; height: 24px; }
  .web-address {
    position: absolute; left: 0; right: 0; bottom: 5px; text-align: center;
    font-size: 7.5px; letter-spacing: 5px; color: #ffffff; font-weight: 500;
  }

  .envelope-back {
    left: 570px; top: 381px; width: 579px; height: 289px;
    background: #f2f2f2;
    box-shadow: 0 2px 10px rgba(0,0,0,0.35);
  }
  .envelope-flap {
    position: absolute; left: 0; top: 0; width: 100%; height: 84px;
    border-radius: 0 0 14px 14px;
    background: linear-gradient(180deg, var(--flap-top), #3b4f72 45%, var(--flap-bottom));
  }

  .envelope-front {
    left: 475px; top: 531px; width: 634px; height: 291px;
    border-top: 1px solid #d8d8d8;
    box-shadow: -2px -3px 10px rgba(0,0,0,0.3), 0 3px 8px rgba(0,0,0,0.3);
  }
  .envelope-front .watermark-area { left: 390px; top: 0; width: 244px; height: 270px; }
  .envelope-front .brand-name { left: 40px; top: 36px; font-size: 36px; }
  .return-address {
    position: absolute; z-index: 1; left: 32px; top: 112px;
    font-size: 7.6px; line-height: 9.6px; color: var(--ink); font-style: normal;
  }
</style>
</head>
<body>

<section class="sheet letterhead">
  <div class="watermark-area" role="img" aria-label="Faint decorative background graphic"></div>
  <div class="brand-name">DORVO</div>
  <address class="contact-block">
    <div class="company">Dorvo Pty Ltd</div>
    <div>PO Box 7214</div>
    <div>Kellan Ridge NSW 2871</div>
    <div>P : 0472 318 605</div>
    <div>E : office@dorvo.com.au</div>
    <div>ABN : 418 276 530</div>
  </address>

  <div class="letter-body">
    <p class="letter-date">Port Aldren, Ocober 12,2015</p>
    <p class="recipient">Sr.<br>MATEO RUIZ<br>Web Master<br>City</p>
    <p class="para">Contrary to popular belief, Lorem Ipsum is not simply random text. It has roots in a piece of classical Latin literature from 45 BC, making it over 2000 years old. Alden Carrow, a Latin professor at Westmere College in Virginia, looked up one of the more obscure Latin words, consectetur, from a Lorem Ipsum passage, and going through the cites of the word in classical literature,</p>
    <p class="para">discovered the undoubtable source. Lorem Ipsum comes from sections 1.10.32 and 1.10.33 of "de Finibus Bonorum et Malorum" (The Extremes of Good and Evil) by Cicero, written in 45 BC. This book is a treatise on the theory of ethics, very popular during the Renaissance. The first line of Lorem Ipsum, "Lorem ipsum dolor sit amet..", comes from a line in section 1.10.32.</p>
    <p class="para">The standard chunk of Lorem Ipsum used since the 1500s is reproduced below for those interested. Sections 1.10.32 and 1.10.33 from "de Finibus Bonorum et Malorum" by Cicero are also reproduced in their exact original form, accompanied by English versions from the 1914 translation by E. Linwood.</p>
    <p class="para">There are many variations of passages of Lorem Ipsum available, but the majority have suffered alteration in some form, by injected humour, or randomised words which don't look even slightly believable. If you are going to use a passage of Lorem Ipsum, you need to be sure there isn't anything embarrassing hidden in the middle of text.</p>
  </div>
  <div class="signature" role="img" aria-label="Handwritten signature"></div>

  <div class="footer-band">
    <svg viewBox="0 0 553 24" preserveAspectRatio="none" aria-hidden="true">
      <rect x="0" y="7" width="553" height="17" fill="var(--brand-blue)"/>
      <polyline points="0,2 68,2 82,12 96,2 553,2" fill="none" stroke="var(--ink-dark)" stroke-width="2.2"/>
      <polyline points="0,5 70,5 82,12 94,5 553,5" fill="none" stroke="#ffffff" stroke-width="1"/>
    </svg>
    <div class="web-address">www.dorvo.com.au</div>
  </div>
</section>

<section class="sheet envelope-back">
  <div class="envelope-flap" role="img" aria-label="Decorative pattern on envelope flap"></div>
</section>

<section class="sheet envelope-front">
  <div class="watermark-area" role="img" aria-label="Faint decorative background graphic"></div>
  <div class="brand-name">DORVO</div>
  <address class="return-address">
    <div class="company">Dorvo Pty Ltd</div>
    <div>PO Box 7214</div>
    <div>Kellan Ridge NSW 2871</div>
  </address>
  <div class="footer-band">
    <svg viewBox="0 0 634 24" preserveAspectRatio="none" aria-hidden="true">
      <rect x="0" y="6" width="634" height="18" fill="var(--brand-blue)"/>
      <polyline points="0,1 56,1 66,11 76,1 634,1" fill="none" stroke="var(--ink-dark)" stroke-width="2.2"/>
      <polyline points="0,4 58,4 66,11 74,4 634,4" fill="none" stroke="#ffffff" stroke-width="1"/>
    </svg>
  </div>
</section>

</body>
</html>
```